Web Button design and production

I need remote control like buttons (or your own design of buttons if I like it)
3x4 text buttons (normal, pressed, disabled)
3x1 empty button (normal, pressed, disabled)
3x6 buttons with glyph (normal, pressed, disabled)
3x288 with 24h time "00:00", "00:05", "00:10" (normal, pressed, disabled)
4 LED (red, green, orange, black)
I will upload the background image as soon as possible (black plastic)
See attached images
Q: Do the buttons have to be gray/black?
A: It should look like a high end remote control. It could be brushed aluminum as well, or something you come up with. But I guess black or dark grey would be best. The background will be pixelvaultimages 40631758, but it's not available yet.
Q: Do I have to provide all buttons for the contest?
A: No! I only need one button (3 states) and a LED to decide. Only the winner will do the whole job.
Q: Is the Designer who wins the contest expected to complete all the extra buttons?
A: Yes, please.
Plastic

```html
<!DOCTYPE html>
<html lang="en">
<head>
<meta charset="utf-8">
<title>Login button states and LED indicators</title>
<link rel="stylesheet" href="https://fonts.googleapis.com/css2?family=Ubuntu:wght@700&display=swap">
<style>
  :root {
    --page: #ffffff;
    --panel-top: #4a494c;
    --panel-bottom: #0c0c0d;
    --label: #1fbf1f;
    --normal-light: #f1ffe0;
    --normal-edge: #d7f7b0;
    --pressed-fill: #d4ff78;
    --pressed-glow: rgba(214, 255, 40, 0.75);
    --disabled-fill: #bfeaa0;
    --disabled-edge: #a8d98a;
  }
  html, body {
    margin: 0;
    padding: 0;
    width: 1200px;
    height: 934px;
    overflow: hidden;
    background: var(--page);
  }
  .canvas {
    position: relative;
    width: 1200px;
    height: 934px;
  }
  .plastic-panel {
    position: absolute;
    left: 64px;
    top: 65px;
    width: 1075px;
    height: 808px;
    background: linear-gradient(180deg, var(--panel-top) 0%, #2a2a2c 45%, var(--panel-bottom) 100%);
  }
  .login-button {
    position: absolute;
    left: 249px;
    width: 236px;
    height: 147px;
    border-radius: 12px;
    box-sizing: border-box;
    display: flex;
    align-items: center;
    justify-content: center;
    font-family: "Ubuntu", sans-serif;
    font-weight: 700;
    font-size: 40px;
    color: var(--label);
  }
  .login-button--normal {
    top: 111px;
    background: radial-gradient(ellipse at center, var(--normal-light) 0%, var(--normal-edge) 100%);
    border: 2px solid #c9eea0;
  }
  .login-button--pressed {
    top: 403px;
    background: var(--pressed-fill);
    border: 2px solid #c6f060;
    box-shadow: 0 0 14px 4px var(--pressed-glow);
  }
  .login-button--disabled {
    top: 690px;
    background: var(--disabled-fill);
    border: 2px solid var(--disabled-edge);
  }
  .led {
    position: absolute;
    left: 620px;
    width: 114px;
    height: 114px;
  }
  .led--off { top: 128px; }
  .led--lit { top: 418px; }
  .led--dim { top: 706px; }
</style>
</head>
<body>
<div class="canvas">
  <div class="plastic-panel"></div>

  <div class="login-button login-button--normal">Login</div>
  <div class="login-button login-button--pressed">Login</div>
  <div class="login-button login-button--disabled">Login</div>

  <svg class="led led--off" viewBox="0 0 114 114" aria-hidden="true">
    <defs>
      <linearGradient id="bezel" x1="0" y1="0" x2="0" y2="1">
        <stop offset="0" stop-color="#ffffff"/>
        <stop offset="0.6" stop-color="#d8d8d8"/>
        <stop offset="1" stop-color="#8a8a8a"/>
      </linearGradient>
      <radialGradient id="lens-red" cx="0.5" cy="0.45" r="0.6">
        <stop offset="0" stop-color="#e0202a"/>
        <stop offset="0.7" stop-color="#b8101a"/>
        <stop offset="1" stop-color="#6e0008"/>
      </radialGradient>
      <radialGradient id="lens-lit" cx="0.5" cy="0.5" r="0.55">
        <stop offset="0" stop-color="#ffffff"/>
        <stop offset="0.25" stop-color="#f4e8e0"/>
        <stop offset="0.6" stop-color="#d86a70"/>
        <stop offset="1" stop-color="#b03038"/>
      </radialGradient>
      <radialGradient id="lens-dim" cx="0.5" cy="0.45" r="0.6">
        <stop offset="0" stop-color="#b8101a"/>
        <stop offset="0.7" stop-color="#8e0810"/>
        <stop offset="1" stop-color="#520006"/>
      </radialGradient>
    </defs>
    <circle cx="57" cy="57" r="56" fill="url(#bezel)"/>
    <circle cx="57" cy="57" r="45" fill="url(#lens-red)"/>
    <ellipse cx="55" cy="36" rx="24" ry="12" fill="#ffffff" opacity="0.45"/>
  </svg>

  <svg class="led led--lit" viewBox="0 0 114 114" aria-hidden="true">
    <circle cx="57" cy="57" r="56" fill="#e8a8ac"/>
    <circle cx="57" cy="57" r="52" fill="url(#bezel)" opacity="0.55"/>
    <circle cx="57" cy="57" r="45" fill="url(#lens-lit)"/>
    <ellipse cx="55" cy="36" rx="22" ry="10" fill="#ffffff" opacity="0.35"/>
  </svg>

  <svg class="led led--dim" viewBox="0 0 114 114" aria-hidden="true">
    <circle cx="57" cy="57" r="56" fill="url(#bezel)"/>
    <circle cx="57" cy="57" r="45" fill="url(#lens-dim)"/>
    <ellipse cx="55" cy="36" rx="24" ry="12" fill="#ffffff" opacity="0.3"/>
  </svg>
</div>
</body>
</html>
```